Corvid Aviation - Learn to Fly

Our customers are people who span all ages and genders that are interested in learning how to fly airplanes for fun or as a career, or who would like to advance their piloting skills.

Flight training we offer:
Private Pilot Certificate
Instrument Rating
Commercial Pilot Certificate
Sport Pilot Certificate: Powered Parachute
Drone Pilot Training

Ground School we offer:
Sport Pilot Ground School
Private Pilot Ground School
Instrument Pilot Ground School
Drone Pilot Ground School

Target Market(s)

Bessemer, Alabama, United States: High school students, college students, career changers. Someone interested in learning to fly for fun or for a career in the United States.

Industry/Entity Type

Aviation

Requirements
Must have
• I would like for you to enjoy some creative freedom here. The feeling and image we want to portray is a professional, but also very exciting and energizing image. The prospective customer and student should see the brochure and be excited to call us or come out for more information on learning how to fly. Our tag line is: "Small Step Today, Giant Leap Tomorrow."
Nice to have
• It would be helpful if you can do some reading or a little research on each of the types of training that we offer so that you will understand what should be included in the brochure. Our goal is to let everyone know who we are, what we offer, and how to contact us.

This may help some with design ideas: The name Corvid Aviation is inspired by the Orbix Skyward space program because the owner of the flight school is a big fan of Orbix and the Skyward mission.

```html
<!DOCTYPE html>
<html lang="en">
<head>
<meta charset="utf-8">
<title>Corvid Aviation – Learn to Fly Brochure</title>
<link rel="stylesheet" href="https://fonts.googleapis.com/css2?family=Montserrat:wght@300;400;600;700;800&family=Open+Sans:wght@400;600&display=swap">
<style>
  :root {
    --navy: #1c2a44;
    --navy-deep: #141f35;
    --red: #d3202f;
    --white: #ffffff;
    --paper: #f7f7f8;
    --ink: #3a3f4a;
    --muted: #8a909c;
    --backdrop: #d9dadc;
  }
  * { box-sizing: border-box; margin: 0; padding: 0; }
  html, body { width: 889px; height: 1200px; overflow: hidden; }
  body {
    background: var(--backdrop);
    font-family: "Open Sans", Arial, sans-serif;
    color: var(--ink);
    position: relative;
  }
  .spread {
    position: absolute;
    left: 44.5px;
    width: 800px;
    height: 566px;
    display: flex;
    background: var(--white);
    box-shadow: 0 6px 18px rgba(0,0,0,.18);
  }
  .spread--outer { top: 22px; }
  .spread--inner { top: 612px; }
  .page { position: relative; width: 400px; height: 566px; overflow: hidden; }
  .page + .page { border-left: 1px solid rgba(0,0,0,.06); }
  .shape { position: absolute; inset: 0; width: 100%; height: 100%; }

  .eyebrow {
    font-family: "Montserrat", sans-serif;
    font-size: 9px; font-weight: 600; letter-spacing: 1px;
    color: var(--red); text-transform: uppercase;
  }
  .heading {
    font-family: "Montserrat", sans-serif;
    font-size: 22px; font-weight: 800; color: var(--navy); line-height: 1.1;
  }
  .heading span { color: var(--red); }
  .body-copy { font-size: 8.5px; line-height: 1.65; color: var(--ink); }

  /* back cover */
  .about-photo {
    position: absolute; top: 0; right: 0; width: 240px; height: 250px;
    background: linear-gradient(90deg, rgba(255,255,255,1) 0%, rgba(255,255,255,0) 40%),
                linear-gradient(160deg, #c9ccd2 0%, #9aa0ab 55%, #6f7683 100%);
  }
  .about-block { position: absolute; top: 32px; left: 30px; width: 200px; }
  .about-block .body-copy { margin-top: 12px; }
  .call-line {
    position: absolute; top: 196px; left: 30px; width: 190px;
    font-family: "Montserrat", sans-serif; font-size: 12px; font-weight: 700;
    color: var(--red); line-height: 1.3;
  }
  .contact-block { position: absolute; top: 330px; left: 30px; color: var(--white); }
  .contact-block .heading { color: var(--white); font-size: 24px; font-weight: 600; margin-bottom: 16px; }
  .contact-list { list-style: none; }
  .contact-list li {
    display: flex; align-items: center; gap: 9px;
    font-size: 9px; margin-bottom: 11px; color: #dfe3ea;
  }
  .contact-list svg { width: 14px; height: 14px; flex: none; }

  .brand-badge {
    position: absolute; border-radius: 50%;
    background: var(--white); border: 3px solid var(--red);
    display: flex; align-items: center; justify-content: center; text-align: center;
    font-family: "Montserrat", sans-serif; font-weight: 800; color: var(--navy);
    text-transform: uppercase; line-height: 1.1;
  }
  .brand-badge--back { width: 72px; height: 72px; top: 400px; left: 300px; font-size: 9px; }
  .brand-badge--front { width: 96px; height: 96px; top: 290px; left: 240px; font-size: 11px; }
  .social-row { position: absolute; bottom: 30px; right: 30px; display: flex; gap: 7px; }
  .social-row span { width: 14px; height: 14px; border-radius: 50%; background: #55627a; }

  /* front cover */
  .cover-photo {
    position: absolute; top: 0; left: 0; width: 400px; height: 360px;
    background: linear-gradient(180deg, #f1d6b0 0%, #d9a86c 35%, #a9793f 65%, #6f5530 100%);
  }
  .tagline {
    position: absolute; top: 418px; right: 34px; text-align: right;
    font-family: "Montserrat", sans-serif; color: var(--white); text-transform: uppercase;
  }
  .tagline__small { font-size: 15px; font-weight: 300; letter-spacing: 1.5px; }
  .tagline__big { font-size: 19px; font-weight: 700; letter-spacing: 1px; margin-top: 2px; }

  /* inner left */
  .who-block { position: absolute; top: 30px; left: 30px; width: 330px; }
  .who-block .body-copy { margin-top: 10px; }
  .services-band {
    position: absolute; top: 140px; left: 0; padding: 6px 30px;
    font-family: "Montserrat", sans-serif; font-size: 15px; font-weight: 700;
    color: var(--white);
  }
  .offer-block { position: absolute; left: 30px; width: 330px; }
  .offer-block--flight { top: 205px; }
  .offer-block--ground { top: 350px; }
  .offer-title {
    font-family: "Montserrat", sans-serif; font-size: 11px; font-weight: 700;
    color: var(--red); text-transform: uppercase; letter-spacing: .5px; margin-bottom: 8px;
  }
  .offer-list { list-style: none; }
  .offer-list li {
    position: relative; padding-left: 14px; font-size: 9.5px; color: var(--ink); margin-bottom: 6px;
  }
  .offer-list li::before {
    content: ""; position: absolute; left: 0; top: 4px;
    width: 6px; height: 6px; background: var(--red); border-radius: 50%;
  }

  /* inner right */
  .quotes { position: absolute; top: 30px; left: 24px; right: 24px; display: flex; gap: 16px; }
  .quote-card {
    flex: 1; height: 190px; border: 1px solid #d6d9de; background: var(--paper);
    padding: 18px 14px; position: relative;
  }
  .quote-card__mark {
    font-family: "Montserrat", sans-serif; font-size: 34px; font-weight: 800;
    color: var(--red); line-height: .6; display: block; margin-bottom: 10px;
  }
  .quote-card__text { font-size: 8.5px; line-height: 1.6; font-style: italic; color: var(--ink); }
  .quote-card__name {
    position: absolute; bottom: 16px; left: 14px;
    font-family: "Montserrat", sans-serif; font-size: 8px; font-weight: 700; color: var(--navy);
  }
  .cockpit-photo {
    position: absolute; left: 0; bottom: 0; width: 400px; height: 300px;
    background: linear-gradient(180deg, #6f8fae 0%, #3c5470 35%, #1f2a38 70%, #121820 100%);
  }
</style>
</head>
<body>

<section class="spread spread--outer">
  <!-- back cover -->
  <article class="page page--back">
    <div class="about-photo" role="img" aria-label="Photo of two smiling pilots in uniform"></div>
    <svg class="shape" viewBox="0 0 400 566" preserveAspectRatio="none" aria-hidden="true">
      <path d="M0 290 Q200 220 400 270 L400 566 L0 566 Z" fill="var(--navy)"/>
      <path d="M0 280 Q200 210 400 262" fill="none" stroke="var(--red)" stroke-width="5"/>
    </svg>
    <div class="about-block">
      <p class="eyebrow">Who We Are</p>
      <h2 class="heading">About <span>Us</span></h2>
      <p class="body-copy">Corvid Aviation is a flight school in Bessemer, Alabama. We train new and returning pilots of every age, from a first discovery flight to a commercial certificate, with patient instructors and well kept aircraft.</p>
    </div>
    <p class="call-line">Call us for more information on learning how to fly.</p>
    <div class="contact-block">
      <h2 class="heading">Contact Us</h2>
      <ul class="contact-list">
        <li><svg viewBox="0 0 16 16"><path d="M4 1.5l2.5 3-1.5 2a8 8 0 0 0 4.5 4.5l2-1.5 3 2.5-1.5 2.5C7 14.5 1.5 9 1.5 3z" fill="var(--red)"/></svg>(205) 555-0148</li>
        <li><svg viewBox="0 0 16 16"><rect x="1.5" y="3.5" width="13" height="9" fill="none" stroke="var(--red)" stroke-width="1.5"/><path d="M1.5 3.5L8 9l6.5-5.5" fill="none" stroke="var(--red)" stroke-width="1.5"/></svg>info@corvidaviation.com</li>
        <li><svg viewBox="0 0 16 16"><path d="M8 15s5-5.2 5-9A5 5 0 0 0 3 6c0 3.8 5 9 5 9z" fill="var(--red)"/><circle cx="8" cy="6" r="1.8" fill="var(--navy)"/></svg>1200 Airport Road, Bessemer, AL</li>
        <li><svg viewBox="0 0 16 16"><circle cx="8" cy="8" r="6.3" fill="none" stroke="var(--red)" stroke-width="1.5"/><path d="M1.7 8h12.6M8 1.7c-3 3.5-3 9.1 0 12.6M8 1.7c3 3.5 3 9.1 0 12.6" fill="none" stroke="var(--red)" stroke-width="1.2"/></svg>www.corvidaviation.com</li>
      </ul>
    </div>
    <div class="brand-badge brand-badge--back">Corvid<br>Aviation</div>
    <div class="social-row" aria-hidden="true"><span></span><span></span><span></span><span></span></div>
  </article>

  <!-- front cover -->
  <article class="page page--front">
    <div class="cover-photo" role="img" aria-label="Photo of a child holding a toy airplane in a sunlit field"></div>
    <svg class="shape" viewBox="0 0 400 566" preserveAspectRatio="none" aria-hidden="true">
      <path d="M0 300 Q220 390 400 320 L400 566 L0 566 Z" fill="var(--navy)"/>
      <path d="M0 292 Q220 382 400 312" fill="none" stroke="var(--red)" stroke-width="5"/>
    </svg>
    <div class="brand-badge brand-badge--front">Corvid<br>Aviation</div>
    <div class="tagline">
      <p class="tagline__small">Small Step Today</p>
      <p class="tagline__big">Giant Leap Tomorrow</p>
    </div>
  </article>
</section>

<section class="spread spread--inner">
  <!-- inner left -->
  <article class="page page--services">
    <svg class="shape" viewBox="0 0 400 566" preserveAspectRatio="none" aria-hidden="true">
      <path d="M0 138 L190 138 Q230 138 250 158 Q270 178 300 178 L0 178 Z" fill="var(--red)"/>
      <path d="M0 520 Q200 490 400 510 L400 566 L0 566 Z" fill="var(--navy)"/>
    </svg>
    <div class="who-block">
      <p class="eyebrow">Our Story</p>
      <h2 class="heading">Who <span>We Are</span></h2>
      <p class="body-copy">Inspired by the Orbix Skyward space program, we believe every great journey starts with one small step. Our instructors guide high school students, college students and career changers toward the cockpit.</p>
    </div>
    <h2 class="services-band">Our Services</h2>
    <div class="offer-block offer-block--flight">
      <h3 class="offer-title">Flight Training We Offer</h3>
      <ul class="offer-list">
        <li>Private Pilot Certificate</li>
        <li>Instrument Rating</li>
        <li>Commercial Pilot Certificate</li>
        <li>Sport Pilot Certificate: Powered Parachute</li>
        <li>Drone Pilot Training</li>
      </ul>
    </div>
    <div class="offer-block offer-block--ground">
      <h3 class="offer-title">Ground School We Offer</h3>
      <ul class="offer-list">
        <li>Sport Pilot Ground School</li>
        <li>Private Pilot Ground School</li>
        <li>Instrument Pilot Ground School</li>
        <li>Drone Pilot Ground School</li>
      </ul>
    </div>
  </article>

  <!-- inner right -->
  <article class="page page--testimonials">
    <div class="quotes">
      <blockquote class="quote-card">
        <span class="quote-card__mark">&ldquo;</span>
        <p class="quote-card__text">My first solo was the best day of my life. The team made every lesson clear and fun.</p>
        <p class="quote-card__name">— Student Pilot</p>
      </blockquote>
      <blockquote class="quote-card">
        <span class="quote-card__mark">&ldquo;</span>
        <p class="quote-card__text">From ground school to my checkride, I always felt ready. Now I fly for a living.</p>
        <p class="quote-card__name">— Commercial Pilot</p>
      </blockquote>
    </div>
    <div class="cockpit-photo" role="img" aria-label="Photo of two pilots seen from behind in an airliner cockpit"></div>
  </article>
</section>

</body>
</html>
```